Ridgeline Haulage Business Card Design

We are a new company base in Far North Queensland Australia called Ridgeline Haulage. We are a company that hire machinery (graders, rollers, excavators and trucks) for road construction and earthworks. We also supply quarry products to the building and construction industries. (Crushed aggregates, road base materials, sand, gravel and rocks). Would like a logo that can also be used on our plant to advertise us.
Target Market(s)
engineers, builders and general public
Industry/Entity Type
Construction
Contact Information for Business Card
Ridgeline Haulage Pty Ltd, Dale and Merryn Vosper
ABN: 38 502 716 904 ACN: 502 716 904
PO Box 19, Cooktown Qld 4895
Pardalote Street Cooktown Qld 4895

```html
<!DOCTYPE html>
<html lang="en">
<head>
<meta charset="utf-8">
<title>Ridgeline Haulage Business Card Design</title>
<link rel="stylesheet" href="https://fonts.googleapis.com/css2?family=Arimo:wght@400;700&display=swap">
<style>
  :root {
    --page: #f4f4f4;
    --card-white: #ffffff;
    --ink: #1a1a1a;
    --orange: #e8821e;
    --panel-dark: #121212;
    --panel-mid: #262626;
    --text-light: #f2f2f2;
    --ghost: #dcdcdc;
    --back-top: #fbfbfb;
    --back-bottom: #ececec;
  }
  * { box-sizing: border-box; margin: 0; padding: 0; }
  html, body {
    width: 1200px;
    height: 900px;
    overflow: hidden;
    background: var(--page);
    font-family: "Arimo", Arial, sans-serif;
  }
  .canvas {
    position: relative;
    width: 1200px;
    height: 900px;
  }
  .card {
    position: absolute;
    top: 291px;
    width: 520px;
    height: 318px;
    border-radius: 24px;
    overflow: hidden;
    box-shadow: 0 10px 28px rgba(0, 0, 0, 0.12);
  }
  .card--front { left: 50px; background: var(--card-white); }
  .card--back {
    left: 630px;
    background: linear-gradient(180deg, var(--back-top), var(--back-bottom));
  }

  .front-header {
    position: absolute;
    inset: 0 0 auto 0;
    height: 148px;
  }
  .brand {
    position: absolute;
    left: 26px;
    top: 42px;
    display: flex;
    align-items: center;
    gap: 12px;
  }
  .brand__mark {
    width: 20px;
    height: 20px;
    background: var(--orange);
  }
  .brand__name {
    font-weight: 700;
    font-size: 32px;
    line-height: 1.05;
    color: var(--ink);
    letter-spacing: 0.5px;
  }
  .owners {
    position: absolute;
    right: 30px;
    top: 28px;
    font-size: 15px;
    color: var(--ink);
  }

  .accent-band {
    position: absolute;
    left: 0; right: 0;
    top: 148px;
    height: 10px;
    background: var(--orange);
  }
  .contact-panel {
    position: absolute;
    left: 0; right: 0;
    top: 158px;
    bottom: 0;
    background: linear-gradient(180deg, var(--panel-mid), var(--panel-dark) 60%);
    padding: 12px 26px;
  }
  .contact-list {
    list-style: none;
    font-size: 13.5px;
    line-height: 17.5px;
    color: var(--text-light);
  }
  .contact-list .label { color: var(--orange); }

  .ghost-name {
    position: absolute;
    left: 0; right: 0;
    top: 50%;
    transform: translateY(-50%);
    text-align: center;
    font-weight: 700;
    font-size: 52px;
    line-height: 1.1;
    color: var(--ghost);
    letter-spacing: 1px;
  }
</style>
</head>
<body>
<main class="canvas">
  <section class="card card--front" aria-label="Business card front">
    <header class="front-header">
      <div class="brand">
        <span class="brand__mark" aria-hidden="true"></span>
        <span class="brand__name">Ridgeline<br>Haulage</span>
      </div>
      <p class="owners">Dale and Merryn Vosper</p>
    </header>
    <div class="accent-band"></div>
    <div class="contact-panel">
      <ul class="contact-list">
        <li><span class="label">Mobile :</span> 04 21 584 730</li>
        <li><span class="label">Ph / Fax:</span> 07 40 318 256</li>
        <li><span class="label">ABN:</span> 38 502 716 904</li>
        <li><span class="label">ACN:</span> 502 716 904</li>
        <li>PO Box 19, Karrawin Qld 4871</li>
        <li>Pardalote Street Karrawin Qld 4871</li>
      </ul>
    </div>
  </section>

  <section class="card card--back" aria-label="Business card back">
    <p class="ghost-name">Ridgeline<br>Haulage</p>
  </section>
</main>
</body>
</html>
```